General Contractors need a new Crisp updated Card Design

We need a new business card design for our company of 25 years based in Toronto call Holvaster Building Inc. : Our goal is to be the leading commercial contractors in Toronto by providing exceptional value to our clients. We work very hard to deliver professional, quality, service in conjunction with consistent price competitiveness to all of our clients on every single project.

Target Market(s)

Design & Build Clients

Industry/Entity Type

Construction Company

Contact Information for Business Card

Address:
18 North Tamlin Glen Road, Unit 57, Marbrook Vale, ON, K7T 2R9
Office: 905-218-5937

Holvasters Logo
Employee Job Description
Employee Cell Phone #
Employee Email
www.holvaster-example.com

Colors

Designer to choose colors to be used in the design.

Requirements
Must have
• Quote Company Saying:
• "Professional. Quality. Service."
Nice to have
• New Crisp up to date look. simple & fresh ( Not to Busy)
Should not have
• NO BLUE PRINTS ON THE BUSINESS CARDS

```html
<!DOCTYPE html>
<html lang="en">
<head>
<meta charset="utf-8">
<title>Holvaster Building Inc. – Business Card</title>
<link rel="stylesheet" href="https://fonts.googleapis.com/css2?family=Roboto+Slab:wght@300;400;700&display=swap">
<style>
  :root {
    --stage: #3a3b3d;
    --brand-green: #006a60;
    --sage: #97b3a8;
    --paper: #ffffff;
    --ink: #3d3d3d;
    --rule: #555555;
  }
  * { box-sizing: border-box; margin: 0; padding: 0; }
  html, body { width: 1200px; height: 900px; overflow: hidden; }
  body {
    background: var(--stage);
    font-family: "Roboto Slab", serif;
    position: relative;
  }
  .card {
    position: absolute;
    left: 250px;
    width: 700px;
    height: 400px;
    overflow: hidden;
  }
  /* Front */
  .card-front {
    top: 35px;
    background: var(--brand-green);
    display: flex;
    flex-direction: column;
    align-items: center;
    justify-content: center;
    gap: 48px;
    color: var(--paper);
  }
  .wordmark {
    display: flex;
    align-items: center;
    gap: 18px;
  }
  .wordmark-square {
    width: 56px;
    height: 56px;
    background: currentColor;
  }
  .wordmark-name {
    font-weight: 400;
    font-size: 40px;
    letter-spacing: 1px;
    line-height: 1;
  }
  .tagline {
    font-weight: 700;
    font-size: 22px;
    letter-spacing: 0.5px;
  }
  /* Back */
  .card-back {
    top: 465px;
    background: var(--paper);
    color: var(--ink);
  }
  .card-back .wordmark {
    position: absolute;
    left: 48px;
    top: 52px;
    color: var(--brand-green);
    gap: 12px;
  }
  .card-back .wordmark-square { width: 36px; height: 36px; }
  .card-back .wordmark-name { font-size: 26px; }
  .divider {
    position: absolute;
    left: 210px;
    right: 48px;
    top: 178px;
    height: 1px;
    background: var(--rule);
  }
  .address {
    position: absolute;
    right: 48px;
    top: 100px;
    text-align: right;
    font-size: 15px;
    line-height: 1.45;
  }
  .person {
    position: absolute;
    left: 48px;
    top: 196px;
  }
  .person-name {
    color: var(--brand-green);
    font-weight: 700;
    font-size: 26px;
    letter-spacing: 0.5px;
  }
  .person-title {
    font-size: 15px;
    margin-top: 2px;
  }
  .person-rule {
    width: 200px;
    height: 1px;
    background: var(--rule);
    margin: 10px 0 12px 0;
  }
  .contact-list { list-style: none; }
  .contact-list li {
    display: flex;
    align-items: center;
    gap: 12px;
    font-size: 16px;
    line-height: 1.55;
  }
  .contact-list svg { width: 14px; height: 14px; fill: var(--brand-green); flex: none; }
  .band-sage {
    position: absolute;
    left: 0;
    bottom: 0;
    width: 430px;
    height: 14px;
    background: var(--sage);
  }
  .band-web {
    position: absolute;
    right: 0;
    bottom: 0;
    width: 262px;
    height: 38px;
    background: var(--brand-green);
    color: var(--paper);
    font-size: 14px;
    display: flex;
    align-items: center;
    justify-content: flex-end;
    padding-right: 20px;
  }
</style>
</head>
<body>
  <section class="card card-front">
    <div class="wordmark">
      <span class="wordmark-square"></span>
      <span class="wordmark-name">HOLVASTER BUILDING INC.</span>
    </div>
    <p class="tagline">Professional. Quality. Service.</p>
  </section>

  <section class="card card-back">
    <div class="wordmark">
      <span class="wordmark-square"></span>
      <span class="wordmark-name">HOLVASTER BUILDING INC.</span>
    </div>

    <address class="address" style="font-style:normal">
      18 North Tamlin Glen Road<br>
      Unit 57, Marbrook Vale<br>
      ON, K7T 2R9
    </address>

    <div class="divider"></div>

    <div class="person">
      <p class="person-name">ROWAN ELLERY</p>
      <p class="person-title">CEO</p>
      <div class="person-rule"></div>
      <ul class="contact-list">
        <li>
          <svg viewBox="0 0 14 14" aria-hidden="true"><path d="M4 0h6a1 1 0 0 1 1 1v12a1 1 0 0 1-1 1H4a1 1 0 0 1-1-1V1a1 1 0 0 1 1-1zm0 2v9h6V2z"/></svg>
          416-555-0148
        </li>
        <li>
          <svg viewBox="0 0 14 14" aria-hidden="true"><path d="M3 0l3 3-2 2c1 2 3 4 5 5l2-2 3 3-2 3C6 13 1 8 0 3z"/></svg>
          905-218-5937
        </li>
        <li>
          <svg viewBox="0 0 14 14" aria-hidden="true"><path d="M0 3h14v1L7 8 0 4zm0 2l7 4 7-4v7H0z"/></svg>
          rellery@holvaster-example.com
        </li>
      </ul>
    </div>

    <div class="band-sage"></div>
    <div class="band-web">www.holvaster-example.com</div>
  </section>
</body>
</html>
```